The Grand Journeys of Tilda Barkaroo and Mabel Moo!

Have you ever wondered how a rescue puppy feels before and after being adopted?
Coming November 2015

The Grand Journeys of Tilda Barkaroo and Mabel Moo, Tilda gets her family

www.tildabarkaroo-example.com sign up to receive updates, special offers and enter contests!

Target Market(s)

children age 4-8, parents of children this age group 30-65

Industry/Entity Type

Publishing Company

Colors
33a6d7
6c459b
a64599

Requirements
Must have
• room for postage, a whimsical feel

```html
<!DOCTYPE html>
<html lang="en">
<head>
<meta charset="utf-8">
<title>The Grand Journeys of Tilda Barkaroo and Mabel Moo – Postcard</title>
<link href="https://fonts.googleapis.com/css2?family=Parisienne&family=Montserrat:wght@700;800&family=Open+Sans:wght@400;600;700&display=swap" rel="stylesheet">
<style>
  :root{
    --blue:#33a6d7;
    --purple:#6c459b;
    --magenta:#a64599;
    --ink:#3a3a3a;
    --rule:#c9c9c9;
    --page:#eeeeee;
    --white:#ffffff;
  }
  *{box-sizing:border-box;margin:0;padding:0}
  html,body{width:900px;height:1200px;overflow:hidden;background:var(--page)}
  body{position:relative;font-family:"Open Sans",sans-serif}

  .postcard{position:absolute;left:40px;width:820px;height:560px;background:var(--white);overflow:hidden;box-shadow:0 2px 8px rgba(0,0,0,.15)}
  .postcard--front{top:30px}
  .postcard--back{top:620px}
  .swoosh{position:absolute;left:0;top:0;width:820px;height:560px}

  /* front */
  .teaser{position:absolute;left:40px;top:26px;width:600px;font-family:"Parisienne",cursive;font-size:34px;line-height:1.2;color:var(--purple)}
  .art{position:absolute;background:linear-gradient(135deg,#f3b23a,#6a3a1c 60%,#f3d28a)}
  .art--butterfly-large{left:620px;top:14px;width:180px;height:140px;border-radius:50% 40% 50% 45%}
  .art--butterfly-small{left:24px;top:160px;width:90px;height:70px;border-radius:50% 40% 50% 45%}
  .title-banner{position:absolute;left:60px;top:206px;width:500px;height:132px;border:3px solid var(--blue);border-radius:60px 0 0 60px;background:var(--white);overflow:hidden}
  .title-banner h1{font-family:"Montserrat",sans-serif;font-weight:800;font-size:20px;line-height:1.15;color:var(--purple);text-transform:uppercase;text-align:center;padding:12px 60px 0 24px}
  .title-banner .subtitle{position:absolute;left:0;right:0;bottom:0;height:36px;background:linear-gradient(90deg,var(--magenta),var(--purple));color:var(--white);font-family:"Parisienne",cursive;font-size:26px;line-height:36px;padding-left:120px}
  .release-badge{position:absolute;left:520px;top:176px;width:180px;height:180px;border-radius:50%;background:var(--white);border:6px solid var(--purple);box-shadow:0 0 0 4px var(--blue);display:flex;align-items:center;justify-content:center;text-align:center;font-family:"Parisienne",cursive;font-size:34px;line-height:1.05;color:var(--purple)}
  .signup{position:absolute;left:0;right:0;top:440px;padding:0 60px;color:var(--white)}
  .signup p{font-family:"Montserrat",sans-serif;font-weight:700;font-size:22px}
  .web{display:flex;align-items:center;gap:10px;margin-top:14px;font-family:"Montserrat",sans-serif;font-weight:700;font-size:18px;letter-spacing:1px;text-transform:uppercase}
  .web svg{flex:none}

  /* back */
  .summary-tab{position:absolute;left:30px;top:36px;padding:6px 18px;background:var(--blue);color:var(--white);border-radius:0 16px 16px 0;font-family:"Montserrat",sans-serif;font-weight:800;font-size:16px}
  .summary{position:absolute;left:30px;top:86px;width:270px;font-size:11.5px;line-height:1.45;color:var(--ink)}
  .summary p{margin-bottom:10px}
  .art--girl-and-puppy{left:305px;top:230px;width:150px;height:235px;border-radius:40% 40% 30% 30%;background:linear-gradient(180deg,#f0c9a6,#b469c2 45%,#7d4aa8 80%,#ffffff)}
  .back-web{position:absolute;left:40px;top:512px;display:flex;align-items:center;gap:8px;color:var(--white);font-family:"Montserrat",sans-serif;font-weight:700;font-size:14px;letter-spacing:1px;text-transform:uppercase}
  .postage-divider{position:absolute;left:480px;top:60px;width:0;height:380px;border-left:1px solid var(--rule)}
  .stamp-box{position:absolute;left:700px;top:40px;width:84px;height:100px;border:1px dashed var(--rule)}
  .address-line{position:absolute;left:510px;width:270px;border-top:1px solid var(--rule)}
</style>
</head>
<body>

<section class="postcard postcard--front">
  <svg class="swoosh" viewBox="0 0 820 560" aria-hidden="true">
    <path d="M0 390 C 220 340, 520 420, 820 360 L820 560 L0 560 Z" fill="var(--blue)"/>
    <path d="M0 410 C 240 370, 520 440, 820 385 L820 560 L0 560 Z" fill="var(--white)"/>
    <path d="M0 420 C 240 385, 520 450, 820 400 L820 560 L0 560 Z" fill="var(--purple)"/>
    <path d="M0 540 C 300 520, 560 560, 820 530 L820 560 L0 560 Z" fill="var(--magenta)"/>
  </svg>

  <p class="teaser">Have you ever wondered how a rescue puppy feels before and after being adopted?</p>
  <div class="art art--butterfly-large" role="img" aria-label="Illustration of a golden butterfly"></div>
  <div class="art art--butterfly-small" role="img" aria-label="Illustration of a small golden butterfly"></div>

  <div class="title-banner">
    <h1>The Grand Journeys of Tilda Barkaroo and Mabel Moo</h1>
    <div class="subtitle">Tilda gets her family</div>
  </div>

  <div class="release-badge">Coming<br>November<br>2015</div>

  <div class="signup">
    <p>Sign up to receive updates Special offers and enter contests!</p>
    <div class="web">
      <svg width="22" height="22" viewBox="0 0 22 22" aria-hidden="true"><circle cx="11" cy="11" r="9.5" fill="none" stroke="#fff" stroke-width="2"/><ellipse cx="11" cy="11" rx="4" ry="9.5" fill="none" stroke="#fff" stroke-width="1.5"/><line x1="1.5" y1="11" x2="20.5" y2="11" stroke="#fff" stroke-width="1.5"/></svg>
      <span>www.tildabarkaroo-example.com</span>
    </div>
  </div>
</section>

<section class="postcard postcard--back">
  <svg class="swoosh" viewBox="0 0 820 560" aria-hidden="true">
    <path d="M0 0 L240 0 C 150 10, 60 20, 0 60 Z" fill="var(--blue)"/>
    <path d="M0 470 C 220 450, 520 500, 820 455 L820 560 L0 560 Z" fill="var(--blue)"/>
    <path d="M0 490 C 240 470, 520 515, 820 475 L820 560 L0 560 Z" fill="var(--purple)"/>
  </svg>

  <div class="summary-tab">SUMMERY</div>
  <div class="summary">
    <p>The Grand Journeys of Tilda Barkaroo and Mabel Moo is a children's book series inspired by the real-life journey of the author's Family as they Fall in love with, adopt, and raise their rescue Puppy.</p>
    <p>The stories are written and illustrated From Tilda Barkaroo's perspective. The design and writing style is intended to provide children with a glimpse of how a dog sees, smells, and Feels the world around them.</p>
    <p>The first two books of the series Focus on the adoption experience and the basic training of both the puppy and Mabel Moo. We hope you enjoy reading our stories with your Family as much as we did creating them.</p>
  </div>

  <div class="art art--girl-and-puppy" role="img" aria-label="Illustration of a girl in a purple dress dancing beside a small black and white puppy"></div>

  <div class="postage-divider"></div>
  <div class="stamp-box"></div>
  <div class="address-line" style="top:270px"></div>
  <div class="address-line" style="top:310px"></div>
  <div class="address-line" style="top:350px"></div>
  <div class="address-line" style="top:390px"></div>

  <div class="back-web">
    <svg width="18" height="18" viewBox="0 0 22 22" aria-hidden="true"><circle cx="11" cy="11" r="9.5" fill="none" stroke="#fff" stroke-width="2"/><ellipse cx="11" cy="11" rx="4" ry="9.5" fill="none" stroke="#fff" stroke-width="1.5"/><line x1="1.5" y1="11" x2="20.5" y2="11" stroke="#fff" stroke-width="1.5"/></svg>
    <span>www.tildabarkaroo-example.com</span>
  </div>
</section>

</body>
</html>
```